BRW (Miriela Vondrash Wellness) Website supporting women to live a healthy lifestyle

Hi
I'm thrilled to be working together to bring a fresh look to my website! As an Integrative Health Practitioner, my mission is to support and empower women on their journey to reclaim their health and well-being. The website should feel inviting, with a soft and nurturing energy that also radiates vibrancy and vitality.

Design & Aesthetic:

I'd love to focus on rich rose gold tones
It should feel soft and approachable yet energetic and lively.

Functional Needs:

The site will support both my coaching services
and product sales, so it’s essential to have an intuitive and user-friendly shopping experience.
I'd love some exciting interactive features that keep visitors engaged and make the journey through the site feel seamless and uplifting.

Please let me know if there’s any additional information you need from me to bring this vision to life!

Thank you for your attention to these details! Here are some ideas I like to see Layout Ideas

Hero Section: An inviting header with a subtle half-moon background for a touch of healing energy.

Navigation & Logo: Place my logo in gold on the top left and use simple navigation links with a rose gold hover effect.

Section Dividers: Use small celestial icons, like a crescent moon, as dividers to create flow and add a bit of magic.

Product & Service Section: A soft rose gold gradient background to highlight products, with circular or wave accents around images.

Footer: Deep rose gold background with a half-moon icon to end with a warm invitation to connect.

Uploading an AI-generated image (it is a bit over the top but it captures the feel I like), with a hint of spirituality and femininity, along with elements like the half moon and colors. :) I'm also uploading my logos, and I have each option available in both color schemes.

Best,
Miriela

• Playfair Display (Headings) & Lora (Body Text)

• Cartwell

```html
<!DOCTYPE html>
<html lang="en">
<head>
<meta charset="utf-8">
<title>BRW — Miriela Vondrash Wellness</title>
<link rel="stylesheet" href="https://fonts.googleapis.com/css2?family=Playfair+Display:wght@400;500&family=Lora:wght@400;600&display=swap">
<style>
:root{
  --ink:#000;
  --rose:#c8605a;
  --rose-deep:#b9504b;
  --rose-soft:#eaa8a2;
  --blush:#fbf5f4;
  --mist:#f0f0f1;
  --text:#2b2222;
  --foot-text:#6b3a3a;
  --white:#fff;
  --gold:#d9a27f;
}
*{margin:0;padding:0;box-sizing:border-box}
html,body{width:1200px;height:2962px;overflow:hidden}
body{position:relative;background:var(--blush);font-family:'Lora',serif;color:var(--text)}
.abs{position:absolute}
h1,h2,h3{font-family:'Playfair Display',serif;font-weight:400}

/* header */
.site-header{position:absolute;left:0;top:0;width:1200px;height:112px;background:var(--ink);z-index:3}
.brand{position:absolute;left:120px;top:16px;display:flex;flex-direction:column;align-items:center;width:140px}
.brand-mark{width:54px;height:54px;border:1.5px solid var(--gold);border-radius:50%;display:flex;align-items:center;justify-content:center;color:var(--gold);font-size:17px}
.brand-name{margin-top:5px;color:var(--gold);font-size:12.5px;white-space:nowrap}
.main-nav{position:absolute;left:462px;top:40px;display:flex}
.main-nav a{font-family:'Playfair Display',serif;font-size:19px;color:var(--white);text-decoration:none;margin-right:36px}
.main-nav a.active,.main-nav a:hover{color:var(--rose-soft)}
.nav-contact{position:absolute;left:959px;top:35px;width:130px;height:40px;border:1.5px solid var(--rose-soft);border-radius:20px;color:var(--white);font-family:'Playfair Display',serif;font-size:19px;display:flex;align-items:center;justify-content:center;text-decoration:none}

/* hero */
.hero{position:absolute;left:0;top:112px;width:1200px;height:490px;background:radial-gradient(ellipse at 80% 15%,#7a1c16 0%,#5a0f0c 45%,#3a0806 100%)}
.hero-title{position:absolute;left:112px;top:46px;width:560px;font-size:37px;line-height:54px;color:var(--white)}
.hero-text{position:absolute;left:112px;top:168px;width:490px;font-size:17px;line-height:34.5px;color:var(--white)}
.btn{display:flex;align-items:center;justify-content:center;font-family:'Playfair Display',serif;text-decoration:none;border-radius:24px}
.btn-solid{background:var(--white);color:var(--rose)}
.btn-line{border:1.5px solid var(--rose);color:var(--rose);background:transparent}
.hero .btn{position:absolute;left:112px;top:333px;width:129px;height:39px;font-size:18px}

/* section headings */
.section-title{position:absolute;left:0;width:1200px;text-align:center;font-size:37px;color:var(--rose)}
.rule{position:absolute;left:528px;width:144px;height:2px;background:var(--rose)}

/* cards */
.card{position:absolute;top:710px;width:312px;height:467px;background:var(--white);border-radius:0 50px 0 50px;box-shadow:0 2px 6px rgba(0,0,0,.08);text-align:center}
.card-photo{width:218px;height:218px;border-radius:50%;border:4px solid var(--rose-deep);margin:37px auto 0}
.card h3{margin-top:30px;font-size:30px;color:var(--rose)}
.card p{margin-top:10px;font-size:15.6px;line-height:33px;padding:0 2px;letter-spacing:-.1px}

/* about */
.about{position:absolute;left:0;top:1342px;width:1200px;height:600px;background:linear-gradient(180deg,#4a0b09 0%,#6a1410 45%,#3c0806 100%)}
.about h2{position:absolute;left:0;top:88px;width:1200px;text-align:center;font-size:37px;color:var(--white)}
.about .rule{background:var(--white);top:144px}
.about p{position:absolute;left:170px;top:176px;width:860px;text-align:center;font-size:16.5px;line-height:34.5px;font-weight:600;color:var(--white)}
.about .btn{position:absolute;left:526px;top:309px;width:149px;height:42px;font-size:18px}

/* programs */
.program{position:absolute;top:2032px;height:148px;text-align:center}
.program svg{display:block;margin:10px auto 0}
.program span{display:block;margin-top:22px;font-family:'Playfair Display',serif;font-size:20px;color:var(--text)}
.divider{position:absolute;top:2032px;width:1px;height:148px;background:#ddd}

/* contact */
.contact{position:absolute;left:0;top:2330px;width:1200px;height:482px;background:var(--mist)}
.contact-mark{position:absolute;left:143px;top:55px;width:145px;height:145px;border:1.5px solid var(--gold);border-radius:50%;display:flex;align-items:center;justify-content:center;font-size:44px;color:var(--gold)}
.contact-item{position:absolute;left:143px;display:flex;align-items:flex-start}
.contact-icon{width:43px;height:43px;border-radius:50%;background:var(--rose-soft);display:flex;align-items:center;justify-content:center;flex:none}
.contact-item span{margin-left:38px;font-size:17.5px;line-height:30px;color:var(--text)}
.contact h2{position:absolute;left:516px;top:34px;font-size:37px;color:var(--rose)}
.form{position:absolute;left:516px;top:103px;width:524px;height:327px;background:var(--white);border-radius:8px;box-shadow:0 1px 5px rgba(0,0,0,.1)}
.field{position:absolute;height:44px;border:1px solid #ddd;font-size:13px;color:#333;padding:14px 15px;background:#fafafa}
.submit{position:absolute;left:21px;top:265px;width:100px;height:32px;font-size:13px;font-family:'Lora',serif}

/* footer */
.site-footer{position:absolute;left:0;top:2812px;width:1200px;height:150px;background:linear-gradient(90deg,#efc4c2 0%,#f0a9a6 55%,#eb9590 100%)}
.foot-row{position:absolute;left:105px;display:flex;font-family:'Playfair Display',serif;font-size:19px;color:var(--foot-text)}
.foot-row span.sep{margin:0 24px}
.social{position:absolute;top:62px;left:990px;display:flex;gap:14px;font-size:14px;color:var(--foot-text)}
</style>
</head>
<body>

<header class="site-header">
  <div class="brand"><div class="brand-mark">BRW</div><div class="brand-name">Miriela Vondrash Wellness</div></div>
  <nav class="main-nav">
    <a class="active" href="#">Home</a><a href="#">Programs</a><a href="#">Labs</a><a href="#">About</a><a href="#">Testimonials</a>
  </nav>
  <a class="nav-contact" href="#">Contact Us</a>
</header>

<section class="hero" role="img" aria-label="Deep red starry night sky with a glowing crescent moon">
  <h1 class="hero-title">Achieve Peak Health, Productivity and Energy with zero Stress</h1>
  <p class="hero-text">The future of medicine is here. We no longer have to guess, but we can test! Functional Medicine tests give you a profound explanation of the symptoms you are experiencing, resulting in fast-forward rebalancing protocols</p>
  <a class="btn btn-solid" href="#">Order Now</a>
</section>
<svg class="abs" style="left:0;top:495px" width="1200" height="110" viewBox="0 0 1200 110" aria-hidden="true">
  <path d="M0 75 Q560 -25 1200 100 L1200 110 L0 110 Z" fill="var(--rose-soft)"/>
  <path d="M90 63 Q640 5 1200 110 L0 110 L0 76 Z" fill="var(--blush)"/>
</svg>

<h2 class="section-title" style="top:592px">Our Products &amp; Services</h2>
<div class="rule" style="top:650px"></div>

<article class="card" style="left:111px">
  <div class="card-photo" role="img" aria-label="Woman eating a healthy snack at home" style="background:linear-gradient(135deg,#e9e4de,#9fa9a4)"></div>
  <h3>Wellness Tools</h3>
  <p>Lorem ipsum dolor sit amet, consectetur adipiscing elit, sed do eiusmod tempor incididunt ut labore.</p>
</article>
<article class="card" style="left:442px">
  <div class="card-photo" role="img" aria-label="Presenter leading a group workshop" style="background:linear-gradient(135deg,#d9d6d1,#4a4644)"></div>
  <h3>Group Workshops</h3>
  <p>Lorem ipsum dolor sit amet, consectetur adipiscing elit, sed do eiusmod tempor incididunt ut labore.</p>
</article>
<article class="card" style="left:773px">
  <div class="card-photo" role="img" aria-label="Women attending a coaching session" style="background:linear-gradient(135deg,#e0a23a,#8a4a3a)"></div>
  <h3>Coaching Sessions</h3>
  <p>Lorem ipsum dolor sit amet, consectetur adipiscing elit, sed do eiusmod tempor incididunt ut labore.</p>
</article>

<a class="btn btn-line abs" href="#" style="left:500px;top:1216px;width:201px;height:43px;font-size:18px">View More Services</a>

<section class="about" role="img" aria-label="Night sky with clouds and crescent moon over dark red mountains">
  <h2>About Miriela Vondrash Wellness</h2>
  <div class="rule"></div>
  <p>Functional Medicine tests give you a profound explanation of the symptoms you are experiencing, resulting in fast-forward rebalancing protocols, customized diets and condition-specific natural supplements– all tailored to your unique physiology.</p>
  <a class="btn btn-solid" href="#">Learn More</a>
</section>
<svg class="abs" style="left:0;top:1825px" width="1200" height="120" viewBox="0 0 1200 120" aria-hidden="true">
  <path d="M0 100 Q600 -40 1200 70 L1200 120 L0 120 Z" fill="var(--rose-soft)"/>
  <path d="M0 120 L0 105 Q560 -10 1110 60 Q1160 66 1200 72 L1200 120 Z" fill="var(--blush)"/>
  <rect y="112" width="1200" height="8" fill="var(--blush)"/>
</svg>

<h2 class="section-title" style="top:1918px">What My Programs Include</h2>
<div class="rule" style="top:1978px"></div>

<div class="program" style="left:105px;width:200px">
  <svg width="70" height="66" viewBox="0 0 70 66" fill="none" stroke="var(--rose)" stroke-width="2"><rect x="6" y="22" width="58" height="34" rx="2"/><path d="M2 60h66"/><circle cx="35" cy="34" r="6"/><path d="M24 52c2-7 20-7 22 0"/><rect x="28" y="2" width="22" height="12" rx="3"/><path d="M33 14l-3 5 7-5"/></svg>
  <span>Zoom Consults</span>
</div>
<div class="divider" style="left:335px"></div>
<div class="program" style="left:362px;width:200px">
  <svg width="70" height="66" viewBox="0 0 70 66" fill="none" stroke="var(--rose)" stroke-width="2"><path d="M20 4h14M23 4v20L8 56a4 4 0 0 0 4 6h30a4 4 0 0 0 4-6L31 24V4"/><path d="M12 44h30"/><rect x="50" y="8" width="10" height="50" rx="5"/><path d="M50 30h10"/></svg>
  <span>Lab Testing</span>
</div>
<div class="divider" style="left:590px"></div>
<div class="program" style="left:628px;width:200px">
  <svg width="70" height="66" viewBox="0 0 70 66" fill="none" stroke="var(--rose)" stroke-width="2"><circle cx="35" cy="34" r="7"/><path d="M24 62c0-9 22-9 22 0"/><circle cx="35" cy="9" r="7"/><circle cx="12" cy="22" r="7"/><circle cx="58" cy="22" r="7"/><circle cx="12" cy="44" r="7"/><circle cx="58" cy="44" r="7"/><path d="M19 25l9 5M51 25l-9 5M19 41l9-4M51 41l-9-4M35 16v11"/></svg>
  <span>Lifestyle Support</span>
</div>
<div class="divider" style="left:883px"></div>
<div class="program" style="left:900px;width:200px">
  <svg width="70" height="66" viewBox="0 0 70 66" fill="none" stroke="var(--rose)" stroke-width="2"><rect x="24" y="2" width="32" height="10" rx="2"/><rect x="22" y="12" width="36" height="50" rx="4"/><path d="M40 46c-8-2-8-12 0-14 8 2 8 12 0 14z"/><ellipse cx="14" cy="52" rx="10" ry="6"/></svg>
  <span>Supplements</span>
</div>

<a class="btn btn-line abs" href="#" style="left:498px;top:2213px;width:205px;height:44px;font-size:18px">View More Programs</a>

<section class="contact">
  <div class="contact-mark">BRW</div>
  <div class="contact-item" style="top:228px">
    <div class="contact-icon"><svg width="20" height="20" viewBox="0 0 24 24" fill="#fff"><path d="M6.6 10.8a15 15 0 0 0 6.6 6.6l2.2-2.2a1 1 0 0 1 1-.25 11.4 11.4 0 0 0 3.6.57 1 1 0 0 1 1 1V20a1 1 0 0 1-1 1A17 17 0 0 1 3 4a1 1 0 0 1 1-1h3.5a1 1 0 0 1 1 1c0 1.25.2 2.45.57 3.57a1 1 0 0 1-.25 1z"/></svg></div>
    <span style="margin-top:6px">+1 555 014 2290</span>
  </div>
  <div class="contact-item" style="top:300px">
    <div class="contact-icon"><svg width="20" height="16" viewBox="0 0 20 16" fill="none" stroke="#fff" stroke-width="1.8"><rect x="1" y="1" width="18" height="14" rx="1"/><path d="M1 2l9 7 9-7"/></svg></div>
    <span style="margin-top:6px">hello@brwellness.au</span>
  </div>
  <div class="contact-item" style="top:392px">
    <div class="contact-icon"><svg width="18" height="22" viewBox="0 0 18 22" fill="none" stroke="#fff" stroke-width="1.8"><path d="M9 21s7-7 7-12A7 7 0 0 0 2 9c0 5 7 12 7 12z"/><circle cx="9" cy="9" r="2.5"/></svg></div>
    <span style="margin-top:-12px">78 lorem lipsum<br>sit amet 987 234</span>
  </div>

  <h2>Contact Us</h2>
  <form class="form">
    <div class="field" style="left:20px;top:27px;width:236px">First Name *</div>
    <div class="field" style="left:272px;top:27px;width:236px">Last Name *</div>
    <div class="field" style="left:20px;top:89px;width:236px">Email Address *</div>
    <div class="field" style="left:272px;top:89px;width:236px">Phone Number *</div>
    <div class="field" style="left:20px;top:149px;width:488px;height:94px">Type Your Message *</div>
    <span class="btn btn-line submit">Submit Now</span>
  </form>
</section>

<footer class="site-footer" role="img" aria-label="Soft rose cloud texture with a half moon">
  <div class="foot-row" style="top:35px"><span>Home</span><span class="sep">|</span><span>Programs</span><span class="sep">|</span><span>Labs</span><span class="sep">|</span><span>About</span><span class="sep">|</span><span>Testimonials</span></div>
  <div class="foot-row" style="top:83px"><span>@2024 Copyrights</span><span class="sep">|</span><span>Privacy</span><span class="sep">|</span><span>Terms &amp; Conditions</span><span class="sep">|</span><span>Disclaimer</span></div>
  <div class="social"><span>Folkly</span><span>Chirpa</span></div>
</footer>

</body>
</html>
```